Poster

I need a poster for my business, www.coastaltablejourneysbay.example which some information about the most important activities (Sangria Tasting, Iberian Ham, Charcuteries & Sherry Wine Tasting, Sailboat Experiences and Picnic Experiences). A3 Format. Social media included (@coastaltablejourneyctj), contact information included.

```html
<!DOCTYPE html>
<html lang="en">
<head>
<meta charset="utf-8">
<title>Coastal Table Journeys Bay – Poster</title>
<link rel="stylesheet" href="https://fonts.googleapis.com/css2?family=Bebas+Neue&family=Montserrat:wght@300;400;600&display=swap">
<style>
  :root {
    --paper: #ffffff;
    --amber: #efa520;
    --amber-line: rgba(255, 255, 255, 0.35);
    --charcoal: #4a4646;
    --ink: #3f3f3f;
    --white: #ffffff;
  }
  * { margin: 0; padding: 0; box-sizing: border-box; }
  html, body {
    width: 900px;
    height: 1200px;
    overflow: hidden;
    background: var(--paper);
  }
  .poster {
    position: relative;
    width: 900px;
    height: 1200px;
    background: var(--paper);
  }
  .brand {
    position: absolute;
    top: 70px;
    left: 0;
    width: 900px;
    display: flex;
    justify-content: center;
    align-items: center;
    gap: 26px;
  }
  .brand-mark {
    width: 22px;
    height: 22px;
    background: var(--amber);
  }
  .brand-name {
    font-family: "Bebas Neue", sans-serif;
    font-size: 62px;
    line-height: 0.95;
    color: var(--ink);
    letter-spacing: 0.5px;
  }
  .activities {
    position: absolute;
    left: 43px;
    top: 240px;
    width: 814px;
    height: 687px;
    background: var(--amber);
  }
  .activity {
    position: absolute;
    left: 0;
    width: 814px;
    text-align: center;
    font-family: "Bebas Neue", sans-serif;
    font-size: 76px;
    line-height: 96px;
    color: var(--white);
  }
  .divider {
    position: absolute;
    left: 90px;
    width: 637px;
    height: 1px;
    background: var(--amber-line);
  }
  .contact {
    position: absolute;
    left: 43px;
    top: 939px;
    width: 814px;
    height: 221px;
    background: var(--charcoal);
    color: var(--white);
    font-family: "Montserrat", sans-serif;
    text-align: center;
  }
  .phone {
    position: absolute;
    top: 22px;
    width: 100%;
    font-size: 54px;
    font-weight: 300;
    line-height: 70px;
  }
  .website {
    position: absolute;
    top: 102px;
    width: 100%;
    font-size: 29px;
    font-weight: 400;
    line-height: 40px;
  }
  .website-domain {
    color: var(--amber);
    font-weight: 600;
  }
  .social {
    position: absolute;
    top: 162px;
    width: 100%;
    font-size: 22px;
    font-weight: 300;
    line-height: 32px;
  }
</style>
</head>
<body>
  <main class="poster">
    <header class="brand">
      <span class="brand-mark"></span>
      <h1 class="brand-name">Coastal Table<br>Journeys Bay</h1>
    </header>

    <section class="activities" role="img" aria-label="Amber panel with a faint pattern of food and drink doodles behind the activity list">
      <h2 class="activity" style="top:22px;">Sangria Tasting</h2>
      <div class="divider" style="top:128px;"></div>
      <h2 class="activity" style="top:140px;">Iberian Ham,<br>Charcuteries &amp; Sherry<br>Wine Tasting</h2>
      <div class="divider" style="top:439px;"></div>
      <h2 class="activity" style="top:449px;">Sailboat Experiences</h2>
      <div class="divider" style="top:560px;"></div>
      <h2 class="activity" style="top:568px;">Picnic Experiences</h2>
    </section>

    <footer class="contact">
      <p class="phone">+34 600 41 27 83</p>
      <p class="website">www.<span class="website-domain">coastaltablejourneysbay</span>.example</p>
      <p class="social">@coastaltablejourneyctj</p>
    </footer>
  </main>
</body>
</html>
```